Therapy Dog Organization Website

Looking for a website that is user friendly, welcoming, dog themed and has the following pages and links:
*Click here to join - links to a jot form
*Click here to donate - links to our paypal page
*Request a visit - links to a jot form
*Facebook Follow Link
*Instagram Follow Link
*Our team - images uploaded to showcase our dogs
*Donors and Referrals Page - Where I can update as donations and referrals come in.
*Online store. Currently this is in Jot Form but I would like a store front. I would not want this to be a link but rather a hidden page, something like www.hollowbirch.org/teamstore.

Please visit www.hollowbirch.org to see what we have right now designed simply in Canva. Dog photos can be provided to use in images.

Note: I have funds from a grant that I have to spend to add gratuity to the project winner.

```html
<!DOCTYPE html>
<html lang="en">
<head>
<meta charset="utf-8">
<title>Hollow Birch Therapy Dogs</title>
<link href="https://fonts.googleapis.com/css2?family=Montserrat:wght@400;500;600;700&family=Caveat:wght@500&display=swap" rel="stylesheet">
<style>
:root{
  --brown:#5a2d0c;
  --brown-dark:#4a2408;
  --orange:#e87e22;
  --orange-soft:#fbe4cc;
  --cream:#f9f6f2;
  --sand:#f5f0ec;
  --footer:#ebe0d8;
  --text:#3b2a1e;
  --muted:#6f5f54;
  --line:#efe4da;
  --white:#ffffff;
}
*{box-sizing:border-box;margin:0;padding:0}
html,body{width:1200px;height:2421px;overflow:hidden}
body{position:relative;background:var(--white);font-family:'Montserrat',sans-serif;color:var(--text)}
a{color:inherit;text-decoration:none}
.abs{position:absolute}

/* header */
.site-header{position:absolute;left:0;top:0;width:1200px;height:75px;background:var(--cream);border-bottom:1px solid var(--line)}
.brand{position:absolute;display:flex;align-items:center;gap:8px;color:var(--orange);font-weight:700;font-size:20px}
.brand-mark{width:22px;height:22px;background:var(--orange);border-radius:4px}
.site-header .brand{left:132px;top:24px}
.main-nav{position:absolute;left:405px;top:30px;display:flex;gap:17px;font-size:11.5px;color:var(--brown)}
.btn{display:inline-flex;align-items:center;justify-content:center;border-radius:20px;font-weight:600;font-size:10.5px}
.btn-dark{background:var(--brown);color:var(--white)}
.btn-light{background:var(--white);color:var(--brown);border:1px solid #e3d7cc}
.header-donate{position:absolute;left:975px;top:22px;width:94px;height:32px}

/* hero */
.hero{position:absolute;left:0;top:75px;width:1200px;height:447px;background:var(--cream);overflow:hidden}
.badge{position:absolute;left:132px;top:96px;height:26px;padding:0 15px;border-radius:13px;background:var(--orange-soft);color:var(--orange);font-size:7.5px;font-weight:600;display:flex;align-items:center;letter-spacing:.2px}
.hero h1{position:absolute;left:134px;top:140px;font-size:32px;line-height:40px;font-weight:600;color:var(--brown);width:500px}
.hero h1 .script{font-family:'Caveat',cursive;color:var(--orange);font-size:46px;font-weight:500}
.hero p{position:absolute;left:134px;top:236px;width:310px;font-size:11.5px;line-height:18.8px;color:var(--muted)}
.hero .join{position:absolute;left:135px;top:317px;width:125px;height:34px}
.hero .visit{position:absolute;left:269px;top:317px;width:119px;height:34px}
.hero-photo{position:absolute;left:598px;top:90px;width:602px;height:357px;background:linear-gradient(90deg,#f1e8df 0%,#e3d2c2 35%,#cbb39c 60%,#b7c9d3 100%);border-radius:200px 0 0 0}

/* section titles */
.section-title{position:absolute;left:0;width:1200px;text-align:center;font-size:18.5px;font-weight:600;color:var(--brown)}
.section-title span{position:relative}
.section-title span::after{content:"";position:absolute;right:-10px;bottom:-7px;width:46px;height:6px;border-bottom:2px solid var(--orange);border-radius:0 0 50% 50%}

/* impact cards */
.impact-card{position:absolute;top:636px;width:294px;height:224px;border:1px solid var(--line);border-radius:22px;background:var(--white);padding:22px}
.icon-box{width:60px;height:58px;border-radius:10px;background:#fcebdc}
.impact-card h3{margin-top:32px;font-size:12.5px;font-weight:600;color:var(--text)}
.impact-card p{margin-top:12px;font-size:11.5px;line-height:18.8px;color:var(--muted)}

/* heroes */
.polaroid{position:absolute;width:204px;height:242px;background:#f7f1ec;border:1px solid #e8d9cc;border-radius:10px;padding:14px 14px 0}
.polaroid .photo{width:100%;height:182px;border-radius:10px}
.polaroid .name{text-align:center;margin-top:14px;font-size:12.5px;color:var(--muted)}
.view-dogs{position:absolute;left:505px;top:1304px;width:192px;height:32px}

/* support */
.support{position:absolute;left:245px;top:1407px;width:710px;height:262px;border-radius:40px;background:var(--orange);overflow:hidden;text-align:center;color:var(--white)}
.support h2{margin-top:64px;font-size:30px;font-weight:600}
.support p{margin:10px auto 0;width:340px;font-size:11.5px;line-height:18.5px;color:#fde6d0}
.amounts{position:absolute;left:209px;top:158px;width:173px;height:42px;border-radius:8px;background:#f09a4d;display:flex;gap:5px;padding:7px}
.amount{flex:1;background:var(--white);color:var(--brown);border-radius:6px;font-size:10px;display:flex;align-items:center;justify-content:center}
.support .donate{position:absolute;left:392px;top:158px;width:108px;height:42px;border-radius:8px;background:var(--white);color:var(--brown);font-size:10.5px;font-weight:600;display:flex;align-items:center;justify-content:center}

/* donors */
.donors{position:absolute;left:0;top:1732px;width:1200px;height:391px;background:var(--sand)}
.col-title{position:absolute;top:58px;font-size:18.5px;font-weight:600;color:var(--brown)}
.donor-card{position:absolute;left:132px;width:450px;height:75px;background:var(--white);border-radius:8px;padding:20px 22px}
.donor-card h4,.partner h4{font-size:12.5px;font-weight:600}
.donor-card p,.partner p{margin-top:6px;font-size:11.5px;color:var(--muted)}
.all-link{position:absolute;left:132px;top:319px;font-size:11.5px;font-weight:600;color:var(--brown);text-decoration:underline}
.referrals{position:absolute;left:618px;top:113px;width:451px;height:214px;border-radius:10px;background:var(--brown);padding:26px 26px;color:var(--white)}
.partner{margin-bottom:28px}
.partner p{color:#e8c9ad}
.referrals .btn-orange{position:absolute;left:27px;top:153px;width:143px;height:31px;border-radius:16px;background:var(--orange);color:var(--white);font-size:10px;font-weight:600;display:flex;align-items:center;justify-content:center}

/* footer */
.site-footer{position:absolute;left:0;top:2123px;width:1200px;height:298px;background:var(--footer)}
.site-footer .brand{left:132px;top:72px;font-size:22px}
.footer-about{position:absolute;left:134px;top:146px;width:230px;font-size:10.5px;line-height:17.5px;color:var(--muted)}
.footer-col{position:absolute;top:70px}
.footer-col h5{font-size:11px;font-weight:600;color:var(--brown);margin-bottom:18px}
.footer-col li{list-style:none;font-size:10px;color:var(--muted);margin-bottom:10px}
.footer-col .lead{font-size:10px;line-height:16px;color:var(--muted);width:180px}
.subscribe{position:absolute;left:891px;top:150px;width:178px;height:33px;border-radius:17px;background:var(--white);border:1px solid #e0d3c8;display:flex;align-items:center;padding-left:16px;font-size:8.5px;color:#a8998d}
.subscribe .go{position:absolute;right:-1px;top:-1px;width:48px;height:33px;border-radius:17px;background:var(--brown);display:flex;align-items:center;justify-content:center}
.footer-rule{position:absolute;left:108px;top:248px;width:982px;height:1px;background:#d9c9bc}
.footer-bottom{position:absolute;left:129px;top:267px;width:942px;display:flex;justify-content:space-between;font-size:10px;color:var(--muted)}
.legal span{margin:0 12px}
</style>
</head>
<body>

<header class="site-header">
  <a class="brand" href="#"><span class="brand-mark"></span>Hollow Birch</a>
  <nav class="main-nav">
    <a href="#">Home</a><a href="#">Our Team</a><a href="#">Donors &amp; Referrals</a><a href="#">Request a Visit</a><a href="#">Services</a>
  </nav>
  <a class="btn btn-dark header-donate" href="#">Donate Now</a>
</header>

<section class="hero">
  <div class="badge">WAGGING TAILS, WARM HEARTS</div>
  <h1>Bringing comfort, joy<br>and unconditional <span class="script">love.</span></h1>
  <p>A Michigan nonprofit dedicated to providing therapy dogs to the community to spread joy, hope and healing — one paw at a time.</p>
  <a class="btn btn-dark join" href="#">Click here to join</a>
  <a class="btn btn-light visit" href="#">Request a visit</a>
  <div class="hero-photo" role="img" aria-label="Photo of a white dog giving its paw to a person's outstretched hand"></div>
</section>

<h2 class="section-title" style="top:580px"><span>Our Paws-itive Impact</span></h2>

<article class="impact-card" style="left:132px">
  <div class="icon-box" role="img" aria-label="Icon of a hand holding a heart"></div>
  <h3>Emotional Support</h3>
  <p>Reducing anxiety and loneliness through gentle, non-judgmental interactions with our furry friends.</p>
</article>
<article class="impact-card" style="left:454px">
  <div class="icon-box" role="img" aria-label="Icon of an open book"></div>
  <h3>School Literacy</h3>
  <p>Helping children build reading confidence in a stress-free environment alongside patient canine listeners.</p>
</article>
<article class="impact-card" style="left:775px">
  <div class="icon-box" role="img" aria-label="Icon of hands holding a group of people"></div>
  <h3>Community Care</h3>
  <p>Providing respite for healthcare workers and first responders dealing with high-stress environments.</p>
</article>

<h2 class="section-title" style="top:928px"><span>Meet Our Furry Heroes</span></h2>

<figure class="polaroid" style="left:146px;top:995px;transform:rotate(-8deg)">
  <div class="photo" role="img" aria-label="Photo of Buster, a black and white shepherd dog" style="background:linear-gradient(135deg,#3a3634,#1c1a19 55%,#d9d3cc)"></div>
  <figcaption class="name">Buster</figcaption>
</figure>
<figure class="polaroid" style="left:390px;top:1013px;transform:rotate(2deg)">
  <div class="photo" role="img" aria-label="Photo of Luna, a dachshund chewing a blue toy" style="background:linear-gradient(135deg,#d9a73a,#9a4f22 55%,#3f8fb8)"></div>
  <figcaption class="name">Luna</figcaption>
</figure>
<figure class="polaroid" style="left:626px;top:995px;transform:rotate(8deg)">
  <div class="photo" role="img" aria-label="Photo of Cooper, a fluffy grey and white dog" style="background:linear-gradient(135deg,#8fa06a,#c9c6c2 55%,#7e8084)"></div>
  <figcaption class="name">Cooper</figcaption>
</figure>
<figure class="polaroid" style="left:860px;top:1063px;transform:rotate(-2deg)">
  <div class="photo" role="img" aria-label="Photo of Daisy, a beagle sitting on grass" style="background:linear-gradient(135deg,#5e8a3a,#7ca84a 50%,#a8744a)"></div>
  <figcaption class="name">Daisy</figcaption>
</figure>

<a class="btn btn-dark view-dogs" href="#">View all certified therapy dogs</a>

<section class="support">
  <h2>Support Our Mission</h2>
  <p>Help us train more dogs and cover travel costs to schools and hospitals across the region.</p>
  <div class="amounts"><span class="amount">$25</span><span class="amount">$50</span><span class="amount">$100</span></div>
  <a class="donate" href="#">Donate Now</a>
</section>

<section class="donors">
  <h2 class="col-title" style="left:132px">Our Generous Donors</h2>
  <h2 class="col-title" style="left:618px">Referral Partners</h2>
  <div class="donor-card" style="top:113px">
    <h4>Emotional Support</h4>
    <p>Cloud phone systems built for reliable business communications.</p>
  </div>
  <div class="donor-card" style="top:206px">
    <h4>Alder Creek Post 17, Veterans Hall</h4>
    <p>Serving veterans from the local community since 1930.</p>
  </div>
  <a class="all-link" href="#">View all donors &amp; referrals</a>
  <div class="referrals">
    <div class="partner">
      <h4>Emotional Support</h4>
      <p>Cloud phone systems built for reliable business communications.</p>
    </div>
    <div class="partner">
      <h4>North Pines Dog Training</h4>
      <p>Building strong bonds between handlers and their dogs.</p>
    </div>
    <a class="btn-orange" href="#">Click here to donate</a>
  </div>
</section>

<footer class="site-footer">
  <a class="brand" href="#"><span class="brand-mark"></span>Hollow Birch</a>
  <p class="footer-about">A Michigan nonprofit dedicated to providing therapy dogs to the community by spreading joy, hope and healing-one paw at a time.</p>
  <div class="footer-col" style="left:555px">
    <h5>Quick Links</h5>
    <ul><li>Home</li><li>Our Team</li><li>Donors &amp; Referrals</li><li>Request a Visit</li><li>Services</li></ul>
  </div>
  <div class="footer-col" style="left:723px">
    <h5>Our Programs</h5>
    <ul><li>Emotional Support</li><li>School Literacy</li><li>Community Care</li><li>Therapy Dog Training</li><li>Volunteer</li></ul>
  </div>
  <div class="footer-col" style="left:891px">
    <h5>Stay Connected</h5>
    <p class="lead">Subscribe to our newsletter for heartwarming stories and updates.</p>
  </div>
  <div class="subscribe">Enter your Email
    <span class="go"><svg width="14" height="10" viewBox="0 0 14 10"><path d="M1 5h11M8 1l4 4-4 4" fill="none" stroke="#fff" stroke-width="1.4" stroke-linecap="round" stroke-linejoin="round"/></svg></span>
  </div>
  <div class="footer-rule"></div>
  <div class="footer-bottom">
    <span>2025 Hollow Birch Therapy Dogs. All rights reserved.</span>
    <span class="legal">Privacy Policy<span>|</span>Terms of Use<span>|</span>Sitemap</span>
  </div>
</footer>

</body>
</html>
```